Banner Ad Design Project

We are a SEO company and need a banner design for our new service, the highlights being:

- Pay Per Performance SEO service
- Guaranteed Frobly page 1 ranking
- Only $197 per month (+ performance bonus)

Can be all on one static banner or made into an animated GIF - designers choice...

Site URL (not up yet) will be RankLoft.com (by Velbrin) - this is a spinoff site of our existing business, Velbrin LLC - logo attached and should be included on the banner.

Industry/Entity Type

Business

Requirements
Must have
• Banner delivered in multiple sizes:
- 200 x 200
- 250 x 250
- 300 x 250
- 336 x 280
- 468 x 60
- 728 x 90
- 120 x 600
- 160 x 600

```html
<!DOCTYPE html>
<html lang="en">
<head>
<meta charset="utf-8">
<title>Velbrin – RankLoft banner set</title>
<link rel="stylesheet" href="https://fonts.googleapis.com/css2?family=Open+Sans:wght@400;600;700&family=Noto+Serif:wght@700&display=swap">
<style>
  :root {
    --stage: #52575b;
    --sky: #9ccbee;
    --sky-deep: #5fa3dc;
    --paper: #ffffff;
    --paper-tint: #e3eef8;
    --ink: #2f3a45;
    --navy: #2b3f8e;
    --leaf: #8cc63f;
    --leaf-dark: #5a9a1e;
    --chart-dark: #3a3d40;
    --bar-track: #eceff1;
    --frame: #d7dde2;
  }
  * { box-sizing: border-box; margin: 0; padding: 0; }
  html, body { width: 1200px; height: 750px; overflow: hidden; }
  body {
    background: var(--stage);
    font-family: "Open Sans", Arial, sans-serif;
    position: relative;
  }
  .banner {
    position: absolute;
    top: 236px;
    width: 335px;
    height: 279px;
    background: var(--sky);
    border: 1px solid var(--frame);
    overflow: hidden;
    color: var(--ink);
  }
  .banner--performance { left: 68px; }
  .banner--ranking { left: 443px; }
  .banner--price { left: 818px; }

  .base-wave { position: absolute; left: 0; top: 0; width: 335px; height: 279px; }

  .headline { position: absolute; left: 19px; top: 15px; line-height: 1; white-space: nowrap; }
  .headline__lead { display: block; font-size: 25.5px; font-weight: 400; letter-spacing: -0.3px; }
  .headline__main { display: block; font-size: 34.5px; font-weight: 400; margin-top: 5px; letter-spacing: -0.4px; }

  .brand {
    position: absolute; left: 22px; top: 208px;
    display: flex; align-items: center; gap: 8px;
  }
  .brand__dot { width: 62px; height: 62px; border-radius: 50%; background: var(--leaf); }
  .brand__name { font-size: 36px; font-weight: 700; color: var(--navy); letter-spacing: -0.5px; line-height: 1; }

  .growth-chart {
    position: absolute; left: 205px; top: 106px; width: 116px; height: 98px;
    background: linear-gradient(160deg, var(--leaf) 0%, #7cbf2b 45%, var(--chart-dark) 100%);
  }

  .rank-meter { position: absolute; left: 143px; top: 130px; width: 176px; height: 56px; }
  .rank-meter__label { position: absolute; left: 40px; top: 4px; font-size: 14px; color: #222; }
  .rank-meter__track { position: absolute; left: 0; top: 25px; width: 176px; height: 28px; background: var(--bar-track); border: 1px solid #cfd4d8; }
  .rank-meter__fill { position: absolute; left: 2px; top: 2px; width: 82px; height: 22px; background: linear-gradient(#9fd45a, var(--leaf-dark)); }
  .rank-meter__value { position: absolute; right: 14px; top: -2px; font-family: "Noto Serif", Georgia, serif; font-weight: 700; font-size: 54px; color: var(--navy); line-height: 1; }

  .price { position: absolute; left: 20px; top: 16px; }
  .price__currency { position: absolute; left: 0; top: 26px; font-size: 24px; }
  .price__amount { position: absolute; left: 17px; top: 2px; font-family: "Noto Serif", Georgia, serif; font-weight: 700; font-size: 64px; color: var(--navy); line-height: 1; letter-spacing: -1px; }
  .price__period { position: absolute; left: 130px; top: 12px; font-size: 23px; white-space: nowrap; }
  .price__bonus { position: absolute; left: 16px; top: 68px; display: flex; align-items: center; gap: 4px; white-space: nowrap; }
  .price__brace { font-size: 26px; font-weight: 400; }
  .price__bonus-text { font-size: 15px; line-height: 1; }
  .price__bonus-text small { display: block; font-size: 14px; }
  .price__bonus-text span { display: block; font-size: 15px; padding-left: 4px; }

  .pay-card {
    position: absolute; left: 192px; top: 80px; width: 133px; height: 150px;
    background: linear-gradient(180deg, #f4f6f8 0%, #d9dee3 100%);
    border-radius: 4px;
  }
</style>
</head>
<body>

  <section class="banner banner--performance">
    <div class="headline">
      <span class="headline__lead">Pay Per Performance</span>
      <span class="headline__main">SEO Service</span>
    </div>
    <div class="growth-chart" role="img" aria-label="Illustration of a rising growth chart"></div>
    <svg class="base-wave" viewBox="0 0 335 279" aria-hidden="true">
      <defs><linearGradient id="paper1" x1="0" y1="0" x2="1" y2="1"><stop offset="0" stop-color="#fff"/><stop offset="1" stop-color="#dbe9f6"/></linearGradient></defs>
      <path d="M0 192 Q170 212 335 188 L335 279 L0 279 Z" fill="var(--sky-deep)"/>
      <path d="M0 200 Q170 216 335 194 L335 279 L0 279 Z" fill="url(#paper1)"/>
    </svg>
    <div class="brand"><span class="brand__dot"></span><span class="brand__name">Velbrin</span></div>
  </section>

  <section class="banner banner--ranking">
    <div class="headline">
      <span class="headline__lead">Guaranteed Frobly</span>
      <span class="headline__main">Page 1 Ranking</span>
    </div>
    <div class="rank-meter">
      <span class="rank-meter__label">RankScore</span>
      <div class="rank-meter__track"><div class="rank-meter__fill"></div></div>
      <span class="rank-meter__value">1</span>
    </div>
    <svg class="base-wave" viewBox="0 0 335 279" aria-hidden="true">
      <defs><linearGradient id="paper2" x1="0" y1="0" x2="1" y2="1"><stop offset="0" stop-color="#fff"/><stop offset="1" stop-color="#dbe9f6"/></linearGradient></defs>
      <path d="M0 192 Q170 212 335 188 L335 279 L0 279 Z" fill="var(--sky-deep)"/>
      <path d="M0 200 Q170 216 335 194 L335 279 L0 279 Z" fill="url(#paper2)"/>
    </svg>
    <div class="brand"><span class="brand__dot"></span><span class="brand__name">Velbrin</span></div>
  </section>

  <section class="banner banner--price">
    <div class="price">
      <span class="price__currency">$</span>
      <span class="price__amount">197</span>
      <span class="price__period">/month only</span>
      <div class="price__bonus">
        <span class="price__brace">{+</span>
        <span class="price__bonus-text"><small>performance</small><span>bonus</span></span>
        <span class="price__brace">}</span>
      </div>
    </div>
    <div class="pay-card" role="img" aria-label="Illustration of a pay card showing $197"></div>
    <svg class="base-wave" viewBox="0 0 335 279" aria-hidden="true">
      <defs><linearGradient id="paper3" x1="0" y1="0" x2="1" y2="1"><stop offset="0" stop-color="#fff" stop-opacity="0.95"/><stop offset="1" stop-color="#dbe9f6" stop-opacity="0.9"/></linearGradient></defs>
      <path d="M0 192 Q170 212 335 188 L335 279 L0 279 Z" fill="var(--sky-deep)"/>
      <path d="M0 200 Q170 216 335 194 L335 279 L0 279 Z" fill="url(#paper3)"/>
    </svg>
    <div class="brand"><span class="brand__dot"></span><span class="brand__name">Velbrin</span></div>
  </section>

</body>
</html>
```